Wine bottle label for family vineyard

Label front and back for our background vineyard. BeLow is a label we used in the past. The gazebo is at the top of the vineyard. We want the front label to have the info we have currently with name etc. But we are open to fun on the back. Maybe a Covid mask would be appropriate Would like one with and one without. But I want the designer to feel free and go out of the box. Especially on back label.

Target Market(s)

None. It’s just for personal consumption We drink what we can and give the rest away.

Industry/Entity Type

Wine

Requirements
Must have
• Name our evening pour. Dunstrom family vineyard. Pinot noir. Year. Name of winemaker.
Nice to have
• The back label being fun is a plus. Maybe some quotes about wine and friends

```html
<!DOCTYPE html>
<html lang="en">
<head>
<meta charset="utf-8">
<title>Our Evening Pour — Dunstrom Family Vineyard Labels</title>
<link rel="stylesheet" href="https://fonts.googleapis.com/css2?family=IM+Fell+English+SC&family=Cormorant+Garamond:wght@400;500&display=swap">
<style>
  :root {
    --backdrop-light: #6a6a6a;
    --backdrop-dark: #1c1c1c;
    --label-paper: #ece8dc;
    --ink: #4a4642;
    --ink-soft: #8f8a82;
    --wine-red: #b3262a;
    --photo-light: #bdbcb6;
    --photo-mid: #94938d;
    --photo-dark: #6e6d68;
  }
  * { box-sizing: border-box; margin: 0; padding: 0; }
  html, body { width: 1200px; height: 900px; overflow: hidden; }
  body {
    background: radial-gradient(ellipse at 50% 35%, var(--backdrop-light), var(--backdrop-dark) 75%);
    display: flex;
    align-items: center;
    justify-content: center;
    gap: 48px;
    font-family: "Cormorant Garamond", serif;
    color: var(--ink);
  }
  .label {
    width: 340px;
    height: 560px;
    background: var(--label-paper);
    display: flex;
    flex-direction: column;
    align-items: center;
    text-align: center;
  }
  .label-back { padding: 56px 40px 36px; }
  .label-front { padding: 52px 36px 28px; }

  .back-artwork {
    width: 166px;
    height: 256px;
    background: linear-gradient(170deg, var(--photo-light), var(--photo-mid) 60%, var(--photo-dark));
  }
  .back-quote {
    margin-top: 34px;
    font-size: 12px;
    line-height: 1.55;
    color: var(--ink-soft);
  }
  .back-signoff {
    margin-top: 12px;
    font-size: 11px;
    color: var(--ink-soft);
    font-style: italic;
  }
  .back-footer {
    margin-top: auto;
    font-size: 9px;
    letter-spacing: 0.12em;
    text-transform: uppercase;
    color: var(--ink-soft);
  }

  .wine-name {
    font-family: "IM Fell English SC", serif;
    font-weight: 400;
    font-size: 34px;
    line-height: 1;
    color: var(--ink);
    white-space: nowrap;
  }
  .title-rule {
    width: 30px;
    height: 1px;
    background: var(--ink-soft);
    margin: 10px 0 8px;
  }
  .vineyard-name {
    font-size: 9px;
    letter-spacing: 0.14em;
    text-transform: uppercase;
    color: var(--ink-soft);
  }
  .gazebo-photo {
    width: 212px;
    height: 160px;
    margin-top: 22px;
    background: linear-gradient(180deg, var(--photo-mid), var(--photo-dark) 45%, var(--photo-light) 80%, var(--photo-light));
  }
  .varietal {
    margin-top: 30px;
    font-family: "IM Fell English SC", serif;
    font-weight: 400;
    font-size: 19px;
    color: var(--ink);
  }
  .estate-mark {
    margin-top: 8px;
    display: flex;
    align-items: center;
    gap: 5px;
    font-size: 11px;
    font-weight: 500;
    letter-spacing: 0.1em;
    text-transform: uppercase;
    color: var(--wine-red);
  }
  .estate-mark .dot {
    width: 6px;
    height: 6px;
    border-radius: 50%;
    background: var(--wine-red);
  }
  .vintage {
    margin-top: 8px;
    font-size: 10px;
    color: var(--ink-soft);
  }
  .winemaker {
    margin-top: auto;
    font-size: 8px;
    letter-spacing: 0.08em;
    text-transform: uppercase;
    color: var(--ink-soft);
    white-space: nowrap;
  }
</style>
</head>
<body>
  <section class="label label-back">
    <div class="back-artwork" role="img" aria-label="Playful sepia painting of a classic portrait wearing a face mask"></div>
    <p class="back-quote">Wine is bottled poetry, and good friends are the reason we open it. Pour a glass, pull up a chair by the gazebo and stay until the stars come out.</p>
    <p class="back-signoff">Share generously</p>
    <p class="back-footer">Estate grown and bottled</p>
  </section>

  <section class="label label-front">
    <h1 class="wine-name">Our Evening Pour</h1>
    <div class="title-rule"></div>
    <p class="vineyard-name">A Dunstrom Family Vineyard</p>
    <div class="gazebo-photo" role="img" aria-label="Black and white photograph of the gazebo at the top of the vineyard"></div>
    <h2 class="varietal">Pinot Noir</h2>
    <p class="estate-mark"><span class="dot"></span>Dunstrom</p>
    <p class="vintage">2016</p>
    <p class="winemaker">Crafted by winemaker Elise Dunstrom, estate bottled</p>
  </section>
</body>
</html>
```